Re-design of current business cards

We are updating our website with new colors and layout. Would like to re-design our business cards to co-ordinate. See attached pdf with new Brindlecraft website colors. We would also like to combine our 2 brands on the one business card. Attached is the new design for our Brindlecraft website, current business cards, which are one sided, brindlecraft logo in tiff, .ai for fonts. Brindlecraft logo font is Optimum, Quillmarsh website home page image, Quillmarsh brand statics for products which includes the logo for this brand.

Quillmarsh brand will stay the dark gray on the website. See attached statics for product and website home page.
Updates

The business cards will be 2 sided. Brindlecraft Brand on one side and Quillmarsh Brand on the other. The colors for Brindlecraft need to follow the color scheme of the brindlecraft website pdf I uploaded. The colors are a blue, lighter teal blue and white. Quillmarsh needs to follow the dark gray color on files uploaded

Target Market(s)

The trade and consumers

Industry/Entity Type

Home Furnishing

Contact Information for Business Card

We are updating our website with new colors and layout. Would like to re-design our business cards to co-ordinate. We would also like to combine our 2 brands onto 1 2 sided business cards.

Requirements
Must have
• Colors that match our new website, see attached image.
• RGB colors
• navy -#152842
• teal - 98aeb9
• The gray color used for Quillmarsh brands.
• ll logos and fonts should stay the same.

```html
<!DOCTYPE html>
<html lang="en">
<head>
<meta charset="utf-8">
<title>Brindlecraft &amp; Quillmarsh Business Cards</title>
<link href="https://fonts.googleapis.com/css2?family=Marcellus&family=Cormorant+Garamond:wght@400;500&display=swap" rel="stylesheet">
<style>
  :root {
    --backdrop: #e4e4e4;
    --card-white: #ffffff;
    --ink: #1e1e1e;
    --ink-soft: #3a3a3a;
    --sage: #6f8a7c;
    --teal: #98aeb9;
    --navy: #152842;
    --charcoal: #3b3b3c;
    --rule-dark: #2a2a2a;
  }
  * { margin: 0; padding: 0; box-sizing: border-box; }
  html, body { width: 1200px; height: 800px; overflow: hidden; }
  body {
    background: var(--backdrop);
    font-family: "Marcellus", "Optima", serif;
    color: var(--ink);
  }
  .canvas {
    position: relative;
    width: 1200px;
    height: 800px;
  }
  .card {
    position: absolute;
    top: 68px;
    width: 380px;
    height: 665px;
    overflow: hidden;
    box-shadow: 0 6px 18px rgba(0,0,0,0.12);
  }

  /* Brindlecraft side */
  .card--brindlecraft { left: 150px; background: var(--card-white); }
  .brand-lockup {
    position: absolute;
    top: 120px;
    left: 0;
    width: 100%;
    text-align: center;
  }
  .brand-mark {
    display: block;
    width: 46px;
    height: 46px;
    margin: 0 auto 10px;
    border-radius: 50%;
    background: var(--sage);
  }
  .brand-name {
    font-size: 36px;
    letter-spacing: 1px;
    color: var(--ink);
    line-height: 1;
  }
  .brand-url {
    display: block;
    margin-top: 6px;
    padding-left: 150px;
    font-size: 9px;
    color: var(--ink);
  }
  .contact {
    position: absolute;
    top: 300px;
    left: 62px;
    width: 270px;
  }
  .contact-name {
    font-size: 19px;
    letter-spacing: 2.5px;
    text-transform: uppercase;
    font-weight: 700;
    -webkit-text-stroke: 0.4px var(--ink);
  }
  .contact-title {
    font-size: 14px;
    color: var(--ink-soft);
    margin-top: 2px;
  }
  .contact-address {
    margin-top: 20px;
    font-size: 14.5px;
    line-height: 1.4;
    color: var(--ink-soft);
  }
  .contact-line {
    font-size: 14.5px;
    color: var(--ink-soft);
    padding: 4px 0;
    border-top: 1.5px solid var(--sage);
  }
  .contact-line:first-of-type { margin-top: 6px; }
  .contact-label { color: var(--sage); letter-spacing: 1px; }
  .card-rule {
    position: absolute;
    left: 0;
    width: 100%;
    height: 3px;
    background: var(--rule-dark);
    top: 590px;
  }
  .card-band {
    position: absolute;
    left: 0;
    bottom: 0;
    width: 100%;
    height: 69px;
    background: var(--teal);
    display: flex;
    align-items: center;
    justify-content: center;
  }
  .band-url {
    color: var(--card-white);
    font-size: 15px;
    letter-spacing: 5px;
  }

  /* Quillmarsh side */
  .card--quillmarsh { left: 670px; background: var(--charcoal); color: var(--card-white); }
  .feature-intro {
    position: absolute;
    top: 34px;
    width: 100%;
    text-align: center;
    font-family: "Cormorant Garamond", serif;
    font-size: 13px;
    letter-spacing: 1px;
  }
  .feature-title {
    position: absolute;
    top: 54px;
    width: 100%;
    text-align: center;
    font-family: "Cormorant Garamond", serif;
    font-size: 40px;
    font-weight: 400;
    letter-spacing: 1.5px;
    text-transform: uppercase;
  }
  .feature-rule {
    position: absolute;
    left: 40px;
    width: 300px;
    height: 5px;
    border-radius: 3px;
    background: var(--card-white);
  }
  .feature-rule--top { top: 110px; }
  .feature-rule--bottom { top: 342px; }
  .feature-photo {
    position: absolute;
    top: 122px;
    left: 62px;
    width: 256px;
    height: 212px;
    background: linear-gradient(160deg, #8a8684 0%, #6d6865 45%, #57524d 75%, #7a6e62 100%);
  }
  .feature-list {
    position: absolute;
    top: 370px;
    width: 100%;
    text-align: center;
    font-family: "Cormorant Garamond", serif;
    font-size: 15px;
    letter-spacing: 1px;
    text-transform: uppercase;
    line-height: 1.3;
    list-style: none;
  }
  .feature-list li + li.gap { margin-top: 10px; }
  .card--quillmarsh .card-band { height: 62px; }
  .band-tagline {
    color: var(--charcoal);
    font-family: "Cormorant Garamond", serif;
    font-size: 15px;
    font-weight: 500;
    letter-spacing: 1px;
    text-transform: uppercase;
  }
</style>
</head>
<body>
<main class="canvas">

  <section class="card card--brindlecraft" aria-label="Brindlecraft side">
    <div class="brand-lockup">
      <span class="brand-mark" aria-hidden="true"></span>
      <div class="brand-name">BRINDLECRAFT</div>
      <span class="brand-url">www.brindlecraft.com</span>
    </div>

    <div class="contact">
      <div class="contact-name">Dana Whitlock</div>
      <div class="contact-title">Graphics/Photography Director</div>
      <div class="contact-address">
        PO BOX 412/1870 Maple Ridge Rd<br>
        Fairhaven, Virginia 24099
      </div>
      <div class="contact-line"><span class="contact-label">P</span> 555.201.4836 | <span class="contact-label">F</span> 555.201.4870</div>
      <div class="contact-line"><span class="contact-label">EMAIL</span> dwhitlock@brindlecraft.com</div>
    </div>

    <div class="card-rule"></div>
    <div class="card-band"><span class="band-url">www.brindlecraft.com</span></div>
  </section>

  <section class="card card--quillmarsh" aria-label="Quillmarsh side">
    <div class="feature-intro">Introducing</div>
    <h1 class="feature-title">Quillmarsh</h1>
    <div class="feature-rule feature-rule--top"></div>
    <div class="feature-photo" role="img" aria-label="Styled interior with framed black-and-white animal prints, a decorative mirror and an upholstered chair"></div>
    <div class="feature-rule feature-rule--bottom"></div>
    <ul class="feature-list">
      <li>Exclusive Designs</li>
      <li>Limited Distribution</li>
      <li>Generous Proportion</li>
      <li class="gap">Limited Introduction</li>
      <li>October 2015</li>
      <li class="gap">Full Collection Launch</li>
      <li>April 2016</li>
    </ul>
    <div class="card-band"><span class="band-tagline">Discover the luxury of home.</span></div>
  </section>

</main>
</body>
</html>
```